Fitness competition business needs a card design

I need a professional business card design using my logo. The card will be horizontal with rounded edges.

Target Market(s)

Female fitness competitors

Industry/Entity Type

Fitness

Contact Information for Business Card

Lise-Anne Korvath
Owner
stagevelora.com
210.555.0137
info@stagevelora.com

Font styles to use
Serif

Colors

Designer to choose colors to be used in the design.

Requirements
Must have
• On the back please add the following:
• Figure
• Bikini
• Physique
• Fitness
Nice to have
• Looking for a very sleek design, contemporary and easy to read.
Should not have
• Should not be difficult to read or be too busy

```html
<!DOCTYPE html>
<html lang="en">
<head>
<meta charset="utf-8">
<title>Stage Velora – Business Card</title>
<link rel="stylesheet" href="https://fonts.googleapis.com/css2?family=Sorts+Mill+Goudy&family=Marcellus&display=swap">
<style>
  :root {
    --backdrop: #2f4047;
    --backdrop-edge: #1f2b31;
    --card: #231f20;
    --ink-light: #f4f2f0;
    --ink-muted: #c9c5c2;
    --accent: #e31e26;
    --steel: #5b5b5d;
  }
  * { box-sizing: border-box; margin: 0; padding: 0; }
  html, body { width: 1200px; height: 900px; overflow: hidden; }
  body {
    background: radial-gradient(ellipse at center, var(--backdrop) 0%, var(--backdrop-edge) 100%);
    display: flex;
    flex-direction: column;
    align-items: center;
    justify-content: center;
    gap: 56px;
    font-family: "Sorts Mill Goudy", Georgia, serif;
  }
  .card {
    position: relative;
    width: 640px;
    height: 366px;
    background: var(--card);
    border-radius: 26px;
    overflow: hidden;
    box-shadow: 0 10px 30px rgba(0,0,0,0.35);
  }

  /* Front */
  .card-front .brand {
    position: absolute;
    left: 64px;
    top: 150px;
    display: flex;
    align-items: center;
    gap: 14px;
  }
  .brand-dot {
    width: 26px; height: 26px;
    border-radius: 50%;
    background: var(--ink-light);
  }
  .card-front .brand-name {
    font-family: "Marcellus", Georgia, serif;
    font-size: 38px;
    letter-spacing: 2px;
    color: var(--ink-light);
  }
  .holder {
    position: absolute;
    left: 380px;
    top: 50px;
    color: var(--ink-light);
  }
  .holder-name { font-size: 20px; letter-spacing: 0.6px; font-weight: 400; }
  .holder-role { font-size: 13px; color: var(--ink-muted); letter-spacing: 0.8px; margin-top: 2px; }
  .contact-list {
    position: absolute;
    left: 380px;
    top: 206px;
    list-style: none;
    color: var(--ink-light);
    font-size: 15px;
    line-height: 23px;
  }
  .contact-list li { display: flex; align-items: center; gap: 12px; }
  .contact-list svg { width: 14px; height: 14px; fill: var(--ink-light); flex: none; }

  /* Back */
  .card-back .brand {
    position: absolute;
    left: 0; right: 0;
    top: 118px;
    display: flex;
    justify-content: center;
    align-items: center;
    gap: 18px;
  }
  .card-back .brand-dot { width: 34px; height: 34px; background: var(--accent); }
  .card-back .brand-name {
    font-family: "Marcellus", Georgia, serif;
    font-size: 58px;
    letter-spacing: 3px;
    color: var(--accent);
  }
  .card-back .rule {
    position: absolute;
    left: 150px; right: 150px;
    top: 214px;
    height: 3px;
    background: var(--steel);
    box-shadow: 0 8px 0 var(--steel);
  }
  .division-band {
    position: absolute;
    left: 0; right: 0; bottom: 0;
    height: 46px;
    background: var(--accent);
    display: flex;
    justify-content: center;
    align-items: center;
    gap: 14px;
    list-style: none;
    color: #fff;
    font-size: 22px;
  }
  .division-band li::before { content: "\2022"; margin-right: 8px; font-size: 18px; }
</style>
</head>
<body>

  <section class="card card-front" aria-label="Card front">
    <div class="brand">
      <span class="brand-dot"></span>
      <span class="brand-name">Stage Velora</span>
    </div>
    <div class="holder">
      <h1 class="holder-name">Lise-Anne Korvath</h1>
      <p class="holder-role">Owner</p>
    </div>
    <ul class="contact-list">
      <li>
        <svg viewBox="0 0 16 16" aria-hidden="true"><path d="M8 1a7 7 0 1 0 0 14A7 7 0 0 0 8 1zm0 1.4c.9 0 1.9 1.5 2.2 4H5.8C6.1 3.9 7.1 2.4 8 2.4zM2.5 7.4h2c0 .1 0 .4 0 .6s0 .5 0 .6h-2a5.6 5.6 0 0 1 0-1.2zm3.3 1.2V7.4h4.4v1.2H5.8zm5.7-1.2h2a5.6 5.6 0 0 1 0 1.2h-2V7.4zM8 13.6c-.9 0-1.9-1.5-2.2-4h4.4c-.3 2.5-1.3 4-2.2 4z"/></svg>
        stagevelora.com
      </li>
      <li>
        <svg viewBox="0 0 16 16" aria-hidden="true"><path d="M3.6 1.5l2.3 2.8-1.3 1.6c.9 1.9 2.5 3.5 4.4 4.5l1.6-1.3 2.9 2.2-1.5 2.2C6.9 13.2 2.6 8.9 1.4 3.3z"/></svg>
        210.555.0137
      </li>
      <li>
        <svg viewBox="0 0 16 16" aria-hidden="true"><path d="M1 3h14v10H1zm1.4 1.3L8 8.6l5.6-4.3z"/></svg>
        info@stagevelora.com
      </li>
    </ul>
  </section>

  <section class="card card-back" aria-label="Card back">
    <div class="brand">
      <span class="brand-dot"></span>
      <span class="brand-name">Stage Velora</span>
    </div>
    <div class="rule"></div>
    <ul class="division-band">
      <li>Figure</li>
      <li>Bikini</li>
      <li>Physique</li>
      <li>Fitness</li>
    </ul>
  </section>

</body>
</html>
```